Employment Agency Website Design

We are working with an employment agency in California.

Some sites to use for content/competitors and inspiration:

https://www.travinmoor.example/us/en
https://www.pelkoworksusa.example
https://www.dunmarhire.example
https://www.vantriga.example/en
https://www.ombrelusa.example
https://www.quilnstaffing.example

Thank you for taking the time to consider designing a website for us. We are web developers based in Stockton, CA, USA. Most of our projects go through the same process. Understanding this process may help you win a project with us. We custom-code all of our websites in-house. We don’t have any requirements as to what tools you use for your design, but we prefer Figma files. For any design that we label as four-stars, we send it to the client for review. The client picks the final design they want us to use. Once we complete this process, we will continue to show additional clients all the four-star sites and purchase them later. Your designs will have multiple chances to sell. For better chances of success, we ask that you follow these guidelines.

IMAGES:
If you use any images or icons in the design, we ask that you have a link to the asset so we can purchase the image/icon. Most of the designs we submit do not have the customer’s images on them unless they have some great images. Be creative; show us the feeling you are trying to portray with your image choices. Use any royalty-free site you choose. We subscribe to Adobe and mainly use their images, but we can purchase images outside of Adobe. PLEASE NOTE: we will not submit designs to clients with watermarks on the images.

FONTS:
We ask that you identify the fonts used in the design. This can be done in a message if you want. We typically use Google Fonts and Adobe Fonts.

CONTENT:
We're always open to different content and ideas. We often submit designs with stock images so the client can see our vision. We typically take pictures after the website launch to use their images with our vision. Lorem Ipsum is fine for paragraphs, but we ask that you write the headers in correct English. We want to be able to show the vision and identify the sections of the website.

INSPIRATION:
We typically add a couple of links in the brief of websites we like to help you get started in your design.

REVISIONS:
We do not often ask for revisions of the designs unless we see something in the design that may not appeal to the client. If there are slight changes that we want to make, we do that in the development process.

FEEDBACK:
We rarely give feedback on designs during the design process. We are working on many website projects and do not have the time to provide feedback. We usually respond if your request is well thought out and asks specific questions, but a note asking “feedback, please” usually goes unanswered.

```html
<!DOCTYPE html>
<html lang="en">
<head>
<meta charset="utf-8">
<title>Veloro Talent – Employment Agency</title>
<link href="https://fonts.googleapis.com/css2?family=Poppins:wght@300;400;500;600;700;800&display=swap" rel="stylesheet">
<style>
:root{
  --red:#d0323a;
  --red-soft:#f9e3e4;
  --ink:#111111;
  --text:#333333;
  --muted:#f0f0f0;
  --white:#ffffff;
  --dark:#000000;
  --line:#cfcfcf;
}
*{box-sizing:border-box;margin:0;padding:0}
html,body{width:1200px;height:4769px;overflow:hidden}
body{font-family:'Poppins',sans-serif;color:var(--text);background:var(--white);position:relative}
section,header,footer{position:absolute;left:0;width:1200px;overflow:hidden}
.abs{position:absolute}
.red{color:var(--red)}
.light{font-weight:400}
h1,h2{font-family:'Poppins',sans-serif;color:var(--ink);font-weight:800;letter-spacing:.2px}
p{font-size:15.5px;line-height:32px}
.btn{position:absolute;display:flex;align-items:center;justify-content:center;border-radius:30px;font-weight:600;font-size:18px;text-decoration:none}
.btn-red{background:var(--red);color:var(--white)}
.btn-outline{border:2px solid var(--white);color:var(--white)}

/* hero */
.hero{top:0;height:654px;background:linear-gradient(180deg,#5b4a3a 0%,#8b6a4a 30%,#6d6258 55%,#45505a 80%,#3a4048 100%)}
.hero-photo{position:absolute;inset:0;background:linear-gradient(115deg,rgba(240,170,100,.35),rgba(60,70,90,.2) 50%,rgba(30,30,40,.55))}
.brand{position:absolute;left:74px;top:18px;display:flex;align-items:center;gap:10px}
.brand-mark{width:18px;height:18px;border-radius:50%;background:var(--red)}
.brand-name{font-size:26px;font-weight:500;color:var(--white)}
.auth a{position:absolute;top:46px;height:40px;border:1.5px solid var(--white);border-radius:20px;color:var(--white);font-size:14px;display:flex;align-items:center;justify-content:center;text-decoration:none}
.nav a{position:absolute;top:110px;color:var(--white);font-size:14px;font-weight:500;text-decoration:none}
.hero h1{position:absolute;left:74px;top:398px;color:var(--white);font-size:48px;line-height:48px}
.field{position:absolute;top:520px;height:58px;background:var(--white);border-radius:3px;font-size:13px;color:#555;display:flex;align-items:center;padding-left:16px}
.search-btn{position:absolute;left:759px;top:520px;width:158px;height:58px;background:var(--red);color:var(--white);font-weight:600;font-size:15px;display:flex;align-items:center;justify-content:center;gap:6px;border-radius:3px}
.opts{position:absolute;top:597px;left:74px;display:flex;gap:26px;color:var(--white);font-size:13.5px}
.opts span{display:flex;align-items:center;gap:10px}

/* candidates */
.candidates{top:654px;height:578px;background:var(--white)}
.candidates h2{position:absolute;left:74px;top:70px;font-size:57px;line-height:60px}
.candidates p{position:absolute;left:74px;top:287px;width:520px}
.person-photo{position:absolute;left:700px;top:16px;width:340px;height:562px;background:linear-gradient(180deg,#6b4a38 0%,#c99a82 25%,#233656 50%,#1c2c48 100%);border-radius:170px 170px 0 0}

/* how */
.how{top:1232px;height:457px;background:var(--muted)}
.how h2,.jobs h2,.stories h2{position:absolute;left:0;width:1200px;text-align:center;font-size:54px}
.how h2{top:50px}
.step{position:absolute;top:151px;width:328px;height:243px;background:var(--white);border-radius:22px;text-align:center;overflow:hidden}
.step svg.icon{position:absolute;left:134px;top:30px}
.step h3{position:absolute;top:108px;width:100%;font-size:19px;font-weight:600;color:var(--ink)}
.step p{position:absolute;top:145px;left:20px;width:288px;font-size:14px;line-height:25px}
.step .num{position:absolute;right:18px;bottom:-30px;font-size:140px;font-weight:800;color:#eeeeee;line-height:1}
.step h3,.step p{z-index:1}

/* jobs */
.jobs{top:1689px;height:632px;background:var(--white)}
.jobs h2{top:75px}
.tabs a{position:absolute;top:175px;font-size:16px;color:var(--ink);text-decoration:none;transform:translateX(-50%);white-space:nowrap}
.tabs a.active{color:var(--red);text-decoration:underline;text-underline-offset:4px}
.cat{position:absolute;width:328px;height:58px;border:1.5px solid var(--line);border-radius:29px;display:flex;align-items:center;padding-left:60px;font-size:14.5px;color:var(--ink)}
.cat svg{position:absolute;left:60px;top:18px}
.cat span{margin-left:40px}

/* about */
.about{top:2321px;height:512px;background:var(--red)}
.about h2{position:absolute;left:74px;top:100px;font-size:56px;line-height:56px;color:var(--white)}
.about p{position:absolute;left:74px;top:238px;width:650px;color:var(--white)}
.about .btn{left:74px;top:352px;width:161px;height:52px}

/* career */
.career{top:2833px;height:497px;background:var(--white)}
.career-photo{position:absolute;left:0;top:0;width:600px;height:497px;background:linear-gradient(100deg,#9aa4ab 0%,#d9d4cc 45%,#eef0f0 80%)}
.career h2{position:absolute;left:617px;top:62px;font-size:56px;line-height:62px}
.career p{position:absolute;left:617px;top:220px;width:530px}
.career .btn{left:617px;top:371px;width:160px;height:52px}

/* stories */
.stories{top:3330px;height:448px;background:linear-gradient(90deg,#5d5550,#2c2a2a 30%,#1f1e1e 70%,#4a4340)}
.stories h2{top:60px;color:var(--white);font-weight:700}
.stories .quote{position:absolute;left:582px;top:152px}
.stories p{position:absolute;left:190px;top:195px;width:820px;text-align:center;color:var(--white);font-size:15.5px}
.stories .name{position:absolute;left:0;width:1200px;top:345px;text-align:center;color:var(--red);font-size:17px;font-weight:600}

/* insights */
.insights{top:3778px;height:589px;background:var(--white)}
.insights h2{position:absolute;left:74px;top:50px;font-size:56px}
.see-all{position:absolute;left:980px;top:70px;font-size:19px;color:var(--red);text-decoration:underline;text-underline-offset:5px}
.post{position:absolute;top:150px;width:328px}
.post-img{width:328px;height:198px;border-radius:4px}
.post .date{margin-top:22px;font-size:14.5px;font-weight:600;color:var(--red)}
.post h3{margin-top:6px;font-size:22px;line-height:30px;font-weight:400;color:var(--ink)}

/* footer */
.footer{top:4367px;height:402px;background:var(--dark);color:var(--white)}
.footer .brand{top:100px;left:74px}
.footer .legal{position:absolute;left:74px;top:208px;font-size:12px;line-height:22px}
.socials{position:absolute;left:74px;top:280px;display:flex;gap:18px}
.socials span{width:18px;height:18px;border-radius:50%;background:var(--white);display:block}
.fcol{position:absolute;top:58px}
.fcol h4{font-size:24px;font-weight:600;margin-bottom:10px}
.fcol a{display:block;color:var(--white);font-size:13px;line-height:37.5px;text-decoration:none}
</style>
</head>
<body>

<header class="hero">
  <div class="hero-photo" role="img" aria-label="Aerial photo of a downtown city skyline at golden hour"></div>
  <div class="brand"><span class="brand-mark"></span><span class="brand-name">veloro talent</span></div>
  <div class="auth">
    <a href="#" style="left:941px;width:72px">log in</a>
    <a href="#" style="left:1035px;width:90px">register</a>
  </div>
  <nav class="nav">
    <a href="#" style="left:478px">home</a>
    <a href="#" style="left:567px">about us</a>
    <a href="#" style="left:680px">job seekers</a>
    <a href="#" style="left:811px">employers</a>
    <a href="#" style="left:939px">insights</a>
    <a href="#" style="left:1045px">contact us</a>
  </nav>
  <h1>search jobs through<br>veloro talent</h1>
  <div class="field" style="left:74px;width:328px">Job title or keyword....</div>
  <div class="field" style="left:430px;width:316px">Location or zip code</div>
  <div class="search-btn">
    <svg width="15" height="15" viewBox="0 0 16 16"><circle cx="6.5" cy="6.5" r="5" fill="none" stroke="#fff" stroke-width="2"/><path d="M10.5 10.5L15 15" stroke="#fff" stroke-width="2.2"/></svg>
    search Job
  </div>
  <div class="opts">
    <span><svg width="14" height="14" viewBox="0 0 16 16"><path d="M15 1L1 7l6 2 2 6z" fill="none" stroke="#fff" stroke-width="1.5" stroke-linejoin="round"/></svg>Use current location</span>
    <span><svg width="13" height="13" viewBox="0 0 14 14"><rect x="1" y="1" width="12" height="12" fill="none" stroke="#fff" stroke-width="1.6"/></svg>remote jobs only</span>
  </div>
</header>

<section class="candidates">
  <svg class="abs" style="left:691px;top:26px" width="480" height="450" viewBox="0 0 480 450"><polygon points="240,0 480,112 480,338 240,450 0,338 0,112" fill="var(--red-soft)"/></svg>
  <div class="person-photo" role="img" aria-label="Photo of a smiling businesswoman in a navy suit with arms crossed"></div>
  <h2>find top<br><span class="red light">candidates</span> to get<br>the <span class="red light">job done</span></h2>
  <p>Sed ut perspiciatis unde omnis iste natus error sit voluptatem accusantium doloremque laudantium, totam rem aperiam, eaque ipsa quae ab illo inventore veritatis et quasi architecto beatae vitae dicta sunt explicabo.</p>
  <a class="btn btn-red" href="#" style="left:74px;top:450px;width:267px;height:53px">search candidates</a>
</section>

<section class="how">
  <h2>how it <span class="red light">works</span></h2>
  <div class="step" style="left:74px">
    <svg class="icon" width="60" height="60" viewBox="0 0 60 60" fill="none" stroke="var(--red)" stroke-width="2"><rect x="10" y="8" width="32" height="44" rx="3"/><rect x="20" y="4" width="12" height="8" rx="2"/><path d="M16 22h4M24 22h12M16 30h4M24 30h12M16 38h4M24 38h8"/><circle cx="44" cy="44" r="9"/><path d="M40 44l3 3 5-6"/></svg>
    <h3>Describe your need</h3>
    <p>Sed ut perspiciatis unde omnis iste natus error sit voluptatem accusantium doloremque laudantium.</p>
    <span class="num">1</span>
  </div>
  <div class="step" style="left:437px">
    <svg class="icon" width="60" height="60" viewBox="0 0 60 60" fill="none" stroke="var(--red)" stroke-width="2"><circle cx="30" cy="14" r="6"/><circle cx="14" cy="26" r="5"/><circle cx="46" cy="26" r="5"/><path d="M20 40c0-8 4-14 10-14s10 6 10 14M6 44c0-6 3-10 8-10M54 44c0-6-3-10-8-10"/><circle cx="30" cy="46" r="8"/><path d="M26 46l3 3 5-6"/></svg>
    <h3>View matching candidates</h3>
    <p>Sed ut perspiciatis unde omnis iste natus error sit voluptatem accusantium doloremque laudantium.</p>
    <span class="num">2</span>
  </div>
  <div class="step" style="left:798px">
    <svg class="icon" width="60" height="60" viewBox="0 0 60 60" fill="none" stroke="var(--red)" stroke-width="2"><circle cx="18" cy="14" r="9"/><circle cx="42" cy="14" r="9"/><circle cx="18" cy="12" r="3"/><circle cx="42" cy="12" r="3"/><path d="M13 20c2-3 8-3 10 0M37 20c2-3 8-3 10 0"/><path d="M8 36l10-6 8 6 8-4 8 4 10-4M14 42l10 8M22 38l10 8M30 36l8 8"/></svg>
    <h3>Connect with a recruiter</h3>
    <p>Sed ut perspiciatis unde omnis iste natus error sit voluptatem accusantium doloremque laudantium.</p>
    <span class="num">3</span>
  </div>
</section>

<section class="jobs">
  <h2>find the <span class="red light">jobs</span></h2>
  <div class="tabs">
    <a href="#" class="active" style="left:265px">Jobs by Industry</a>
    <a href="#" style="left:456px">Jobs by State</a>
    <a href="#" style="left:633px">Jobs by Type</a>
    <a href="#" style="left:880px">Jobs by Featured Companies</a>
  </div>

  <div class="cat" style="left:74px;top:242px"><svg width="20" height="20" viewBox="0 0 20 20"><rect x="3" y="1" width="14" height="18" rx="2" fill="var(--red)"/><rect x="5" y="3" width="10" height="4" fill="#fff"/><path d="M6 10h2M9 10h2M12 10h2M6 13h2M9 13h2M12 13h2M6 16h2M9 16h2M12 16h2" stroke="#fff" stroke-width="1.6"/></svg><span>Accounting &amp; Finance</span></div>
  <div class="cat" style="left:437px;top:242px"><svg width="20" height="20" viewBox="0 0 20 20"><rect x="4" y="1" width="12" height="18" fill="var(--red)"/><path d="M7 4h2M11 4h2M7 8h2M11 8h2M7 12h2M11 12h2" stroke="#fff" stroke-width="1.6"/></svg><span>Hospitality</span></div>
  <div class="cat" style="left:798px;top:242px"><svg width="22" height="20" viewBox="0 0 22 20"><path d="M1 2h4l3 11h11l2-8H7" fill="var(--red)"/><circle cx="9" cy="17" r="2" fill="var(--red)"/><circle cx="17" cy="17" r="2" fill="var(--red)"/></svg><span>Retail</span></div>

  <div class="cat" style="left:74px;top:320px"><svg width="22" height="20" viewBox="0 0 22 20"><ellipse cx="9" cy="8" rx="8" ry="6" fill="var(--red)"/><ellipse cx="14" cy="12" rx="7" ry="5" fill="var(--red)"/></svg><span>Customer Services</span></div>
  <div class="cat" style="left:437px;top:320px"><svg width="24" height="20" viewBox="0 0 24 20"><circle cx="12" cy="6" r="4" fill="var(--red)"/><circle cx="5" cy="8" r="3" fill="var(--red)"/><circle cx="19" cy="8" r="3" fill="var(--red)"/><path d="M5 18a7 7 0 0114 0zM0 16a5 5 0 018-2zM24 16a5 5 0 00-8-2z" fill="var(--red)"/></svg><span>Human Resources</span></div>
  <div class="cat" style="left:798px;top:320px"><svg width="24" height="20" viewBox="0 0 24 20"><path d="M1 4h13v10H1zM14 7h5l4 4v3h-9z" fill="var(--red)"/><circle cx="6" cy="16" r="2.5" fill="var(--red)"/><circle cx="18" cy="16" r="2.5" fill="var(--red)"/></svg><span>Transportation</span></div>

  <div class="cat" style="left:74px;top:398px"><svg width="20" height="20" viewBox="0 0 20 20"><circle cx="10" cy="8" r="6" fill="var(--red)"/><rect x="7" y="14" width="6" height="4" rx="1" fill="var(--red)"/></svg><span>Creative &amp; Marketing</span></div>
  <div class="cat" style="left:437px;top:398px"><svg width="20" height="20" viewBox="0 0 20 20"><path d="M12 2a5 5 0 00-1 6L2 16l2 2 8-9a5 5 0 006-1l-3-1-1-3z" fill="var(--red)"/></svg><span>Industrial &amp; Manufacturing</span></div>
  <div class="cat" style="left:798px;top:398px"><svg width="22" height="20" viewBox="0 0 22 20"><path d="M7 2l5 2.5v5L7 12 2 9.5v-5zM15 8l5 2.5v5L15 18l-5-2.5v-5zM5 11l4 2v4l-4 2-4-2v-4z" fill="none" stroke="var(--red)" stroke-width="1.8"/></svg><span>Warehousing</span></div>

  <div class="cat" style="left:74px;top:479px"><svg width="28" height="20" viewBox="0 0 28 20"><circle cx="9" cy="11" r="6" fill="none" stroke="var(--red)" stroke-width="4" stroke-dasharray="3 2"/><circle cx="21" cy="6" r="4" fill="none" stroke="var(--red)" stroke-width="3" stroke-dasharray="2 1.5"/></svg><span>Engineering &amp; Technology</span></div>
  <div class="cat" style="left:437px;top:479px"><svg width="20" height="20" viewBox="0 0 20 20"><rect x="3" y="3" width="14" height="16" fill="var(--red)"/><rect x="7" y="1" width="6" height="4" fill="var(--red)"/><path d="M10 8v7M6.5 11.5h7" stroke="#fff" stroke-width="2"/></svg><span>Medical &amp; Science</span></div>
  <div class="cat" style="left:798px;top:479px"><svg width="22" height="20" viewBox="0 0 22 20"><rect x="1" y="5" width="20" height="13" rx="2" fill="var(--red)"/><path d="M8 5V2h6v3" fill="none" stroke="var(--red)" stroke-width="2"/><path d="M5 5v13M17 5v13" stroke="#fff" stroke-width="1.5"/></svg><span>Office &amp; Administrative</span></div>
</section>

<section class="about">
  <h2>about veloro<br><span class="light">talent</span></h2>
  <p>Sed ut perspiciatis unde omnis iste natus error sit voluptatem accusantium doloremque laudantium, totam rem aperiam, eaque ipsa quae ab illo inventore veritatis et quasi architecto beatae vitae dicta sunt explicabo.</p>
  <a class="btn btn-outline" href="#">learn more</a>
  <svg class="abs" style="left:763px;top:55px" width="364" height="402" viewBox="0 0 364 402" role="img" aria-label="Hexagon photo of a diverse team smiling together at work">
    <defs><linearGradient id="teamTone" x1="0" y1="0" x2="1" y2="1"><stop offset="0" stop-color="#6b5445"/><stop offset=".5" stop-color="#c9b8ad"/><stop offset="1" stop-color="#eae6e3"/></linearGradient></defs>
    <polygon points="182,0 364,100 364,302 182,402 0,302 0,100" fill="url(#teamTone)"/>
  </svg>
</section>

<section class="career">
  <div class="career-photo" role="img" aria-label="Photo of a thoughtful young man in glasses working at a bright office desk"></div>
  <h2>Make the <span class="red light">career</span><br>move <span class="red light">you</span> want</h2>
  <p>Sed ut perspiciatis unde omnis iste natus error sit voluptatem accusantium doloremque laudantium, totam rem aperiam, eaque ipsa quae ab illo inventore veritatis et quasi architecto beatae vitae dicta sunt explicabo.</p>
  <a class="btn btn-red" href="#">learn more</a>
</section>

<section class="stories" role="img" aria-label="Darkened photo of colleagues shaking hands in a meeting">
  <h2>explore success <span class="light">stories</span></h2>
  <svg class="quote" width="36" height="30" viewBox="0 0 36 30"><path d="M2 2h13v13l-6 13H3l5-13H2zM20 2h13v13l-6 13h-6l5-13h-6z" fill="#fff"/></svg>
  <p>Sed ut perspiciatis unde omnis iste natus error sit voluptatem accusantium &nbsp;doloremque laudantium, totam rem aperiam, eaque ipsa quae ab illo inventore veritatis et quasi architecto beatae vitae dicta sunt explicabo. Excepteur sint occaecat cupidatat non proident, sunt in culpa qui officia deserunt mollit anim id est laborum."</p>
  <div class="name">Name Heading</div>
</section>

<section class="insights">
  <h2>discover more <span class="red light">insights</span></h2>
  <a class="see-all" href="#">see all articles</a>
  <article class="post" style="left:74px">
    <div class="post-img" role="img" aria-label="Photo of two colleagues talking in a modern lounge" style="background:linear-gradient(160deg,#e9ece9,#c8cfca 45%,#a8553a 80%,#7a3a28)"></div>
    <div class="date">Mar 01, 2024</div>
    <h3>Sed ut perspiciatis unde omnis iste natus error sit voluptatem accusantium doloremque laudantium...</h3>
  </article>
  <article class="post" style="left:437px">
    <div class="post-img" role="img" aria-label="Photo of a smiling professional holding a folder in an office" style="background:linear-gradient(160deg,#dfe6ee,#b8c6d6 40%,#2b4264 75%,#1e2f4a)"></div>
    <div class="date">Mar 01, 2024</div>
    <h3>Sed ut perspiciatis unde omnis iste natus error sit voluptatem accusantium doloremque laudantium...</h3>
  </article>
  <article class="post" style="left:798px">
    <div class="post-img" role="img" aria-label="Photo of a confident businesswoman in a white blazer at the office" style="background:linear-gradient(160deg,#6f7b80,#b5bcbe 40%,#ece9e6 75%,#d8d2cc)"></div>
    <div class="date">Mar 01, 2024</div>
    <h3>Sed ut perspiciatis unde omnis iste natus error sit voluptatem accusantium doloremque laudantium...</h3>
  </article>
</section>

<footer class="footer">
  <div class="brand"><span class="brand-mark"></span><span class="brand-name">veloro talent</span></div>
  <div class="legal">Copyright © 2024 CompanyName<br>All Rights Reserved</div>
  <div class="socials" aria-label="Social links"><span></span><span></span><span></span><span></span><span></span></div>
  <div class="fcol" style="left:343px"><h4>company</h4><a href="#">Excepteur sint</a><a href="#">Occaecat cupidatat</a><a href="#">Proidentsunt</a><a href="#">Culpa qui officia</a><a href="#">Deserunt mollit</a><a href="#">Anim id est laboru</a></div>
  <div class="fcol" style="left:617px"><h4>services</h4><a href="#">Excepteur sint</a><a href="#">Occaecat cupidatat</a><a href="#">Proidentsunt</a><a href="#">Culpa qui officia</a><a href="#">Deserunt mollit</a><a href="#">Anim id est laboru</a></div>
  <div class="fcol" style="left:883px"><h4>resources</h4><a href="#">Excepteur sint</a><a href="#">Occaecat cupidatat</a><a href="#">Proidentsunt</a></div>
  <div class="fcol" style="left:883px;top:218px"><h4>support</h4><a href="#">Excepteur sint</a><a href="#">Occaecat cupidatat</a><a href="#">Proidentsunt</a></div>
</footer>

</body>
</html>
```